Online shopping portal - Business Card Design

Brightcart.com.au is a complete shopping experience. Search, compare & buy items from partnered stores & receive cashbash for your purchases and referrals.
Mission
Our mission is to provide a system for entrepreneurs to create an ongoing income, while providing consumers worldwide with a better way to shop.
A product brokerage and Internet marketing company that specialises in One-to-One Marketing, Velora Oceania is a subsidiary of Velora Continental Holdings, Inc.
With more than 3 million Preferred Customers and 180,000 Customer Managers worldwide, Velora Continental has generated over $3 billion USD in accumulated retail sales. The Company employs more than 675 people globally with international operations in Australia, United States, Canada, Taiwan, Hong Kong, Mexico & Singapore
Through revolutionary technology and the one-to-one marketing and social shopping Velora Oceania are leveraging the Internet with the power of people to create the economy of the future.
By providing online shoppers with the products and services they want and need — backed by the Company’s people power — Velora Oceania is fast becoming the World Wide Web’s ultimate online shopping destination.
As a result, we are changing the way people shop and changing the economic paradigm where anyone can become financially independent by creating their own economy — Rooted in Goods. Driven by Folks®.
Description
Welcome to a new kind of comparison shopping site where you get PAID cashback to shop!
Simply create an account to start accumulating cash backs each time you make purchases across hundreds of trusted Partner Stores and thousands of your favorite brands through our convenient MonoBag® for one stop shopping.
All merchant stores are backed by BUYNEST.COM's 100% satisfaction guarantee.

Updates
Project Deadline Extended
Reason: Hi all,  I am extending the deadline as i'm going to be away for my birthday (and may not have time to check before the current deadline anyway)  I figure that the more time i give you the better.

Industry/Entity Type
Online Shopping
Contact Information for Business Card
Business Name: Brightcart.com.au
website: www.brightcart.com.au
Facebook: www.facebook.com/brightcart.com.au.
Email: info@brightcart.com.au
Phone: Quin on 0438 72 15 94
Requirements
Nice to have
- Create a Brightcart logo

```html
<!DOCTYPE html>
<html lang="en">
<head>
<meta charset="utf-8">
<title>Brightcart – Business Card</title>
<link href="https://fonts.googleapis.com/css2?family=Exo+2:wght@400;500;800&display=swap" rel="stylesheet">
<style>
  :root {
    --page-bg: #e6e8ea;
    --card-white: #ffffff;
    --card-shade: #e9ecee;
    --blue-light: #19d6ea;
    --blue-mid: #12a9d9;
    --blue-deep: #0e7fc0;
    --accent-swoosh: #1b6fb3;
    --brand-blue: #1a86cc;
    --ink: #1f2a36;
    --ink-name: #143a5a;
  }
  * { box-sizing: border-box; margin: 0; padding: 0; }
  html, body { width: 1200px; height: 864px; overflow: hidden; }
  body {
    background: var(--page-bg);
    font-family: "Exo 2", sans-serif;
    position: relative;
  }
  .business-card {
    position: absolute;
    left: 100px; top: 146px;
    width: 1000px; height: 572px;
    background: radial-gradient(ellipse at 58% 32%, var(--card-white) 0%, var(--card-white) 35%, var(--card-shade) 100%);
    box-shadow: 0 6px 24px rgba(0,0,0,0.12);
    overflow: hidden;
  }
  .card-waves { position: absolute; inset: 0; }
  .brand-name {
    position: absolute;
    right: 70px; top: 70px;
    font-weight: 800;
    font-size: 66px;
    letter-spacing: 1px;
    color: var(--brand-blue);
    line-height: 1;
  }
  .contact-block {
    position: absolute;
    right: 70px; top: 162px;
    text-align: right;
    color: var(--ink);
    font-size: 20px;
    line-height: 1.25;
  }
  .address { margin-bottom: 22px; margin-right: 34px; }
  .contact-line {
    display: flex;
    justify-content: flex-end;
    align-items: center;
    gap: 12px;
    margin-bottom: 12px;
    font-size: 19px;
  }
  .contact-line svg { width: 22px; height: 22px; flex: none; }
  .person {
    position: absolute;
    left: 62px; bottom: 62px;
    color: var(--ink-name);
  }
  .person-name { font-size: 34px; font-weight: 500; letter-spacing: 1px; }
  .person-role { font-size: 23px; margin-left: 40px; }
</style>
</head>
<body>
  <div class="business-card">
    <svg class="card-waves" viewBox="0 0 1000 572" preserveAspectRatio="none">
      <defs>
        <radialGradient id="blueField" cx="0.5" cy="0.45" r="0.7">
          <stop offset="0" stop-color="var(--blue-light)"/>
          <stop offset="0.55" stop-color="var(--blue-mid)"/>
          <stop offset="1" stop-color="var(--blue-deep)"/>
        </radialGradient>
      </defs>
      <path d="M0,215 C80,195 130,240 175,300 C240,385 420,420 640,420 C800,420 920,405 1000,395 L1000,572 L0,572 Z" fill="url(#blueField)"/>
      <path d="M60,205 C110,200 150,250 190,300 C250,375 420,405 640,408 C780,410 900,400 1000,392 C900,398 780,402 640,400 C430,396 270,370 210,300 C170,255 130,210 60,205 Z" fill="var(--accent-swoosh)"/>
    </svg>

    <div class="brand-name">BRIGHTCART</div>

    <div class="contact-block">
      <div class="address">214 9th floor Plaza<br>Harbour Lane KWS</div>
      <div class="contact-line">0438 72 15 94
        <svg viewBox="0 0 24 24"><path d="M6 3 L9 3 L10 8 L8 9.5 C9 12 11.5 14.8 14.5 16 L16 14 L21 15 L21 18 C21 19.5 20 20.5 18.5 20.5 C10 20 4 14 3.5 5.5 C3.5 4 4.5 3 6 3 Z" fill="var(--ink)"/></svg>
      </div>
      <div class="contact-line">0438 72 15 94
        <svg viewBox="0 0 24 24"><rect x="7" y="2" width="10" height="20" rx="2" fill="none" stroke="var(--ink)" stroke-width="2"/><circle cx="12" cy="18" r="1.2" fill="var(--ink)"/></svg>
      </div>
      <div class="contact-line">0438 72 15 94
        <svg viewBox="0 0 24 24"><rect x="3" y="9" width="18" height="12" rx="1.5" fill="var(--ink)"/><rect x="7" y="3" width="10" height="7" fill="none" stroke="var(--ink)" stroke-width="2"/></svg>
      </div>
      <div class="contact-line">info@brightcart.com.au
        <svg viewBox="0 0 24 24"><rect x="2" y="5" width="20" height="14" rx="1.5" fill="var(--ink)"/><path d="M3 6 L12 13 L21 6" fill="none" stroke="#fff" stroke-width="1.5"/></svg>
      </div>
      <div class="contact-line">www.brightcart.com.au
        <svg viewBox="0 0 24 24"><circle cx="12" cy="12" r="9.5" fill="none" stroke="var(--ink)" stroke-width="2"/><ellipse cx="12" cy="12" rx="4" ry="9.5" fill="none" stroke="var(--ink)" stroke-width="1.5"/><path d="M2.5 12 H21.5 M4.5 7 H19.5 M4.5 17 H19.5" stroke="var(--ink)" stroke-width="1.5"/></svg>
      </div>
    </div>

    <div class="person">
      <div class="person-name">QUIN HARLOW</div>
      <div class="person-role">Managing Director</div>
    </div>
  </div>
</body>
</html>
```